Stationery Design Project for Holloway Kenbukan Karate Studio

We Need a Stationery Design for a Karate School Teaching Okinawa Shorin Ryu Karate in Fernhollow, Ohio, U.S.A.

Target Market(s)

Adults Base Western Speaking aged between 25 and 65 yrs, old that handle household budgets

Industry/Entity Type

School

Requirements
Must have
• Name of business: Holloway Kenbukan Karate Studio
Address: Larkspur Commons 18342 US Hwy. 91
Fernhollow, Ohio. 33914
Phone # : 407-555-0183
email : Hollowaykenbukanstudio@mailgrove.example
Logo - attatched

```html
<!DOCTYPE html>
<html lang="en">
<head>
<meta charset="utf-8">
<title>Holloway Kenbukan Karate Studio – Business Card</title>
<link rel="stylesheet" href="https://fonts.googleapis.com/css2?family=Raleway:wght@400;500;700&display=swap">
<style>
  :root {
    --karate-red: #b01e24;
    --ink: #1f1f1f;
    --card-white: #e9e9e9;
    --backdrop: #d8d5d0;
    --muted: #3a3a3a;
  }
  * { margin: 0; padding: 0; box-sizing: border-box; }
  html, body {
    width: 1200px; height: 900px; overflow: hidden;
    background: var(--backdrop);
    font-family: "Raleway", sans-serif;
    color: var(--ink);
  }
  .canvas {
    width: 1200px; height: 900px;
    display: flex; flex-direction: column;
    align-items: center; justify-content: center; gap: 56px;
  }
  .card {
    width: 640px; height: 366px;
    position: relative;
    box-shadow: 0 6px 18px rgba(0,0,0,0.18);
  }
  .card--front {
    background: var(--karate-red);
    display: flex; align-items: center; justify-content: center;
  }
  .brand {
    display: flex; align-items: center; gap: 16px;
  }
  .brand__dot {
    width: 34px; height: 34px; border-radius: 50%;
    background: var(--ink);
    flex-shrink: 0;
  }
  .brand__name {
    font-weight: 700; color: var(--ink);
    text-transform: uppercase; line-height: 1.05;
    letter-spacing: 0.02em;
  }
  .card--front .brand__name { font-size: 34px; }
  .card--back {
    background: var(--card-white);
    border-top: 22px solid var(--karate-red);
    border-bottom: 22px solid var(--karate-red);
    display: flex;
  }
  .card--back .brand {
    width: 270px; padding-left: 34px;
  }
  .card--back .brand__name { font-size: 22px; }
  .card--back .brand__dot { width: 26px; height: 26px; background: var(--karate-red); }
  .details {
    flex: 1; padding-top: 40px; padding-right: 28px;
  }
  .details__name {
    font-size: 24px; font-weight: 400; text-transform: uppercase;
    letter-spacing: 0.01em; padding-left: 4px; padding-bottom: 10px;
    border-bottom: 1.5px solid var(--karate-red);
  }
  .details__role {
    font-size: 14px; color: var(--muted);
    padding: 8px 0 0 4px;
  }
  .contact {
    list-style: none; margin-top: 22px; padding-left: 4px;
    font-size: 14px; line-height: 1.55; color: var(--muted);
  }
  .contact__key {
    display: inline-block; width: 20px;
    color: var(--karate-red); font-weight: 500;
  }
  .address {
    font-style: normal; margin-top: 20px; padding-left: 24px;
    font-size: 14px; line-height: 1.55; color: var(--muted);
  }
</style>
</head>
<body>
<main class="canvas">
  <section class="card card--front" aria-label="Card front">
    <div class="brand">
      <span class="brand__dot"></span>
      <span class="brand__name">Holloway<br>Kenbukan<br>Karate</span>
    </div>
  </section>

  <section class="card card--back" aria-label="Card back">
    <div class="brand">
      <span class="brand__dot"></span>
      <span class="brand__name">Holloway<br>Kenbukan<br>Karate</span>
    </div>
    <div class="details">
      <h1 class="details__name">Sensei Marcus T. Okafor</h1>
      <p class="details__role">Instructor</p>
      <ul class="contact">
        <li><span class="contact__key">T</span>407-555-0183</li>
        <li><span class="contact__key">E</span>Hollowaykenbukanstudio@mailgrove.example</li>
      </ul>
      <address class="address">
        Holloway Kenbukan Karate Studio<br>
        Larkspur Commons<br>
        18342 US Hwy. 91<br>
        Fernhollow, Ohio. 33914
      </address>
    </div>
  </section>
</main>
</body>
</html>
```